4.25" x 11" Door Hanger Design - Glass Bolt Internet Service

We are sourcing a door hanger that will be used to micro target specific neighborhoods with our new "Glass Bolt" internet service offering

This will be used as a template for a new type of plan we are offering in very specific areas. The first will be "Cedar Hollow" with 3 plan offerings.

Stock photos should be family friendly but we want something modern and exciting that we can use to advertise a new internet service offering.
Updates

Sorry if I missed this before, but we would of course like our website and phone number with an encouragement to call us Website: www.brivanet.example Phone: 555-304-2968

Target Market(s)

Residential Internet Service

Industry/Entity Type

Internet Service Provider

Font styles to use
Sans Serif
Other font styles liked:
• RockoFLF

Colors

Designer to choose colors to be used in the design.

Requirements
Must have
• 1) Our logo with "Internet Services" nearby to show "Brivanet Internet Services" (name and what we do)
• 2) "Glass Bolt Internet Service is Now Available in Cedar Hollow!"
• 3) Show three plans, we don't know the price yet and we will edit the winning design eventually when we know the exact price.
• 100 Mbps $XX.XX per month
• 250 Mbps $XX.XX per month
• 1 Gbps $XX.XX per month
• 4) The plan names and prices should be easy to edit in the future if/when we try these in different markets.
• This ad will be modified with specific information like prices and the location when we use it in specific spots.
• We will be using Printwagon for the printing, please use their website for the punch hole location, dimensions, etc.
• https://www.printwagon.example/door-hanger-printing/
Nice to have
• We want to demonstrate far higher than normal internet service speed offerings. This can use whatever you think demonstrates this idea to the customers better, something like a speed test looking logo
Should not have
• Do not copy our website, we want a fresh design

```html
<!DOCTYPE html>
<html lang="en">
<head>
<meta charset="utf-8">
<title>Brivanet Door Hanger – Glass Bolt</title>
<link href="https://fonts.googleapis.com/css2?family=Fira+Sans:wght@400;500;600&family=Tinos&display=swap" rel="stylesheet">
<style>
  :root {
    --stage: #9c9c9c;
    --brand-blue: #2e8fd8;
    --sky: #8dc3ea;
    --sky-deep: #3d9be0;
    --ink: #1b1b1b;
    --ink-soft: #3a3a3a;
    --paper: #ececec;
    --night: #000000;
    --slate: #2b2d38;
    --white: #ffffff;
    --label: #6f6f6f;
  }
  html, body {
    margin: 0;
    width: 1200px;
    height: 1200px;
    overflow: hidden;
    background: var(--stage);
    font-family: "Fira Sans", sans-serif;
  }
  .stage { position: relative; width: 1200px; height: 1200px; }
  .hanger { position: absolute; top: 37px; width: 410px; height: 1026px; }
  .hanger--light { left: 120px; }
  .hanger--dark { left: 670px; }
  .variant-label {
    position: absolute; top: 1118px; width: 40px; text-align: center;
    font-family: "Tinos", serif; font-size: 30px; color: var(--label);
  }
  .variant-label--a { left: 292px; }
  .variant-label--b { left: 842px; }

  .brand-name { font-family: "Fira Sans", sans-serif; font-weight: 400; font-size: 84px; fill: var(--brand-blue); }
  .brand-dot { fill: var(--brand-blue); }
  .tagline { font-family: "Fira Sans", sans-serif; font-weight: 600; font-size: 37px; }
  .headline { font-family: "Fira Sans", sans-serif; font-weight: 600; font-size: 30px; }
  .subline { font-family: "Fira Sans", sans-serif; font-weight: 500; font-size: 24px; }
  .price-title { font-family: "Fira Sans", sans-serif; font-weight: 600; font-size: 30px; }
  .plan-speed, .plan-price { font-family: "Fira Sans", sans-serif; font-weight: 500; font-size: 32px; fill: var(--white); }
  .plan-unit { font-size: 21px; }
  .body-copy { font-family: "Fira Sans", sans-serif; font-weight: 500; font-size: 19px; }
  .hole { fill: var(--stage); stroke: #7e7e7e; stroke-width: 1; }
</style>
</head>
<body>
<main class="stage">

  <!-- Variant A: light body -->
  <svg class="hanger hanger--light" viewBox="0 0 512 1282" xmlns="http://www.w3.org/2000/svg">
    <defs>
      <linearGradient id="a-wedge" x1="0" y1="0" x2="1" y2="0">
        <stop offset="0" stop-color="#2e8fd8"/><stop offset="1" stop-color="#8dc3ea"/>
      </linearGradient>
      <linearGradient id="a-wedge-bottom" x1="0" y1="0" x2="1" y2="0">
        <stop offset="0" stop-color="#8dc3ea"/><stop offset="1" stop-color="#2e8fd8"/>
      </linearGradient>
      <linearGradient id="a-photo" x1="0" y1="0" x2="1" y2="1">
        <stop offset="0" stop-color="#7fb3e6"/><stop offset="0.5" stop-color="#2f6fc4"/><stop offset="1" stop-color="#12388f"/>
      </linearGradient>
      <linearGradient id="a-row-dark" x1="0" y1="0" x2="1" y2="0">
        <stop offset="0" stop-color="#000"/><stop offset="1" stop-color="#6d6d6d"/>
      </linearGradient>
      <linearGradient id="a-row-light" x1="0" y1="0" x2="1" y2="0">
        <stop offset="0" stop-color="#6d6d6d"/><stop offset="1" stop-color="#000"/>
      </linearGradient>
    </defs>

    <rect class="sheet" width="512" height="1282" fill="var(--paper)"/>
    <rect class="header" width="512" height="399" fill="var(--night)"/>
    <polygon class="corner-wedge" points="0,0 482,0 0,104" fill="url(#a-wedge)"/>
    <circle class="hole" cx="257" cy="132" r="72"/>

    <circle class="brand-dot" cx="60" cy="288" r="12"/>
    <text class="brand-name" x="275" y="312" text-anchor="middle">Brivanet</text>
    <text class="tagline" x="256" y="377" text-anchor="middle" fill="var(--white)">INTERNET SERVICES</text>

    <text class="headline" x="256" y="440" text-anchor="middle" fill="var(--ink-soft)">GLASS BOLT INTERNET SERVICE</text>
    <text class="subline" x="256" y="472" text-anchor="middle" fill="var(--ink-soft)">is Now Available in Cedar Hollow!</text>

    <g class="feature-banner">
      <polygon points="484,512 490,512 440,792 425,779" fill="#8a8a8a"/>
      <polygon points="290,779 372,790 298,930 288,930 330,840" fill="#8a8a8a"/>
      <polygon points="170,779 352,779 330,835 262,940 278,832 180,815" fill="var(--brand-blue)"/>
      <polygon points="262,779 352,779 330,835 280,832" fill="var(--sky)"/>
      <polygon points="30,519 478,499 425,779 68,779" fill="url(#a-photo)" role="img" aria-label="Stock photo: woman surrounded by floating app and media icons in blue tones"/>
    </g>

    <text class="price-title" x="45" y="930" fill="var(--ink-soft)">PRICE.</text>

    <g class="plan-table">
      <rect y="944" width="512" height="42" fill="url(#a-row-dark)"/>
      <rect y="987" width="512" height="42" fill="url(#a-row-light)"/>
      <rect y="1030" width="512" height="41" fill="url(#a-row-dark)"/>
      <polygon points="58,955 67,965 58,975" fill="var(--white)"/>
      <polygon points="58,998 67,1008 58,1018" fill="var(--white)"/>
      <polygon points="58,1040 67,1050 58,1060" fill="var(--white)"/>
      <text class="plan-speed" x="78" y="976">100 Mbps</text>
      <text class="plan-speed" x="78" y="1019">250 Mbps</text>
      <text class="plan-speed" x="78" y="1061">1 Gbps</text>
      <text class="plan-price" x="255" y="976">$XX.XX <tspan class="plan-unit">per month</tspan></text>
      <text class="plan-price" x="255" y="1019">$XX.XX <tspan class="plan-unit">per month</tspan></text>
      <text class="plan-price" x="255" y="1061">$XX.XX <tspan class="plan-unit">per month</tspan></text>
    </g>

    <g class="body-copy" fill="var(--ink)">
      <text x="46" y="1117" textLength="420" lengthAdjust="spacing">We want to demonstrate far higher than normal</text>
      <text x="46" y="1140" textLength="420" lengthAdjust="spacing">internet service speed offerings. This can use</text>
      <text x="46" y="1163" textLength="420" lengthAdjust="spacing">whatever you think demonstrates this idea to</text>
      <text x="46" y="1186" textLength="420" lengthAdjust="spacing">the customers better, something like a speed</text>
      <text x="46" y="1208">test looking logo</text>
    </g>

    <polygon class="corner-wedge" points="512,1184 512,1282 0,1282" fill="url(#a-wedge-bottom)"/>
  </svg>

  <!-- Variant B: dark body -->
  <svg class="hanger hanger--dark" viewBox="0 0 512 1282" xmlns="http://www.w3.org/2000/svg">
    <defs>
      <linearGradient id="b-wedge" x1="0" y1="0" x2="1" y2="0">
        <stop offset="0" stop-color="#2e8fd8"/><stop offset="1" stop-color="#8dc3ea"/>
      </linearGradient>
      <linearGradient id="b-wedge-bottom" x1="0" y1="0" x2="1" y2="0">
        <stop offset="0" stop-color="#8dc3ea"/><stop offset="1" stop-color="#2e8fd8"/>
      </linearGradient>
      <linearGradient id="b-photo" x1="0" y1="0" x2="1" y2="1">
        <stop offset="0" stop-color="#7fb3e6"/><stop offset="0.5" stop-color="#2f6fc4"/><stop offset="1" stop-color="#12388f"/>
      </linearGradient>
      <linearGradient id="b-footer" x1="0" y1="0" x2="0" y2="1">
        <stop offset="0" stop-color="#8dc3ea"/><stop offset="1" stop-color="#7db8e6"/>
      </linearGradient>
    </defs>

    <rect class="sheet" width="512" height="1282" fill="var(--slate)"/>
    <polygon class="corner-wedge" points="0,0 482,0 0,104" fill="url(#b-wedge)"/>
    <circle class="hole" cx="257" cy="132" r="72"/>

    <circle class="brand-dot" cx="60" cy="288" r="12"/>
    <text class="brand-name" x="275" y="312" text-anchor="middle">Brivanet</text>
    <rect class="tagline-band" y="341" width="512" height="46" fill="var(--sky)"/>
    <text class="tagline" x="256" y="377" text-anchor="middle" fill="var(--ink)">INTERNET SERVICES</text>

    <text class="headline" x="256" y="440" text-anchor="middle" fill="var(--white)">GLASS BOLT INTERNET SERVICE</text>
    <text class="subline" x="256" y="472" text-anchor="middle" fill="var(--white)">is Now Available in Cedar Hollow!</text>

    <g class="feature-banner">
      <polygon points="484,512 490,512 440,792 425,779" fill="#1c1d25"/>
      <polygon points="170,779 352,779 330,835 262,940 278,832 180,815" fill="var(--brand-blue)"/>
      <polygon points="262,779 352,779 330,835 280,832" fill="var(--sky)"/>
      <polygon points="30,519 478,499 425,779 68,779" fill="url(#b-photo)" role="img" aria-label="Stock photo: woman surrounded by floating app and media icons in blue tones"/>
    </g>

    <text class="price-title" x="45" y="930" fill="var(--white)">PRICE.</text>

    <g class="plan-table">
      <rect y="944" width="512" height="42" fill="#5aabe6"/>
      <rect y="987" width="512" height="42" fill="#8cc4ec"/>
      <rect y="1030" width="512" height="41" fill="var(--sky-deep)"/>
      <polygon points="58,955 67,965 58,975" fill="var(--white)"/>
      <polygon points="58,998 67,1008 58,1018" fill="var(--white)"/>
      <polygon points="58,1040 67,1050 58,1060" fill="var(--white)"/>
      <text class="plan-speed" x="78" y="976">100 Mbps</text>
      <text class="plan-speed" x="78" y="1019">250 Mbps</text>
      <text class="plan-speed" x="78" y="1061">1 Gbps</text>
      <text class="plan-price" x="255" y="976">$XX.XX <tspan class="plan-unit">per month</tspan></text>
      <text class="plan-price" x="255" y="1019">$XX.XX <tspan class="plan-unit">per month</tspan></text>
      <text class="plan-price" x="255" y="1061">$XX.XX <tspan class="plan-unit">per month</tspan></text>
    </g>

    <rect class="footer-panel" y="1085" width="512" height="197" fill="url(#b-footer)"/>
    <g class="body-copy" fill="var(--ink)">
      <text x="46" y="1117" textLength="420" lengthAdjust="spacing">We want to demonstrate far higher than normal</text>
      <text x="46" y="1140" textLength="420" lengthAdjust="spacing">internet service speed offerings. This can use</text>
      <text x="46" y="1163" textLength="420" lengthAdjust="spacing">whatever you think demonstrates this idea to</text>
      <text x="46" y="1186" textLength="420" lengthAdjust="spacing">the customers better, something like a speed</text>
      <text x="46" y="1208">test looking logo</text>
    </g>

    <polygon class="corner-wedge" points="512,1184 512,1282 0,1282" fill="url(#b-wedge-bottom)"/>
  </svg>

  <div class="variant-label variant-label--a">A</div>
  <div class="variant-label variant-label--b">B</div>
</main>
</body>
</html>
```